Business Card Design - Construction Company

Torvane Construction is in need of a sharp, modern business card design that has an architectural/high fashion feel.

We are looking for a two sided card.

One side simple dark grey/black with some texture in the background. e.g. (a mosaic of simple interconnecting shapes or a shadow of the logo.) Something to draw attention and create interest.It will need to feature a large Torvane construction logo (files attached) in metallic gradient or plain white.

The other side should contain all of our information:

(in largest text)
Name of person
Torvane Construction Pty. Ltd.

Licensed builders specialising in:
- Bathrooms
- Kitchens
- Commercial interiors

(mid sized text)
Phone number
Fax number
person@torvaneconstruction.example.au
www. torvaneconstruction.example.au

(smaller text)
ABN: 47209836512
BSA license: xxx-xxxx
PO Box 8640 Dunmore QLD 4170 (address)

Target Market(s)

professional home and business owners

Industry/Entity Type

Construction

Requirements
Must have
• Must be bold, professional looking and modern.
Nice to have
• We are undecided as to what kind of printing we will go with.
Definitely square edged.
Probably high quality satin card.
We are also interested in designs that would work well on transparent or translucent plastic.
Ideally we would print two versions.
Should not have
• Nothing with an antique feel.
No wild colours. Small amounts of colour can be good in the right place.

```html
<!DOCTYPE html>
<html lang="en">
<head>
<meta charset="utf-8">
<title>Torvane Construction – Business Cards</title>
<link rel="stylesheet" href="https://fonts.googleapis.com/css2?family=Play:wght@400;700&display=swap">
<style>
  :root {
    --stage: #2b2b2b;
    --ink-dark: #0b0b0b;
    --ink-light: #ffffff;
    --silver: #c9c9c9;
    --silver-dark: #6e6e6e;
    --text-on-dark: #f2f2f2;
    --text-on-light: #1a1a1a;
    --muted-on-dark: #bdbdbd;
    --muted-on-light: #9a9a9a;
  }
  * { box-sizing: border-box; margin: 0; padding: 0; }
  html, body { width: 1200px; height: 900px; overflow: hidden; }
  body {
    position: relative;
    background: var(--stage);
    font-family: "Play", sans-serif;
  }
  .card { position: absolute; overflow: hidden; }

  /* Front faces */
  .front-dark {
    left: 38px; top: 40px; width: 548px; height: 297px;
    background:
      radial-gradient(ellipse 62% 95% at 50% 50%, #000 0 88%, transparent 92%),
      repeating-linear-gradient(180deg, #8a8a8a 0 2px, #b5b5b5 2px 4px, #6f6f6f 4px 5px, #9e9e9e 5px 7px);
  }
  .front-light {
    left: 625px; top: 40px; width: 540px; height: 293px;
    background:
      radial-gradient(ellipse 62% 95% at 50% 50%, #fff 0 80%, rgba(255,255,255,0) 95%),
      repeating-linear-gradient(180deg, #9a9a9a 0 2px, #cfcfcf 2px 4px, #7c7c7c 4px 5px, #b4b4b4 5px 7px);
  }
  .front-name {
    position: absolute; left: 0; right: 0; top: 56%;
    transform: translateY(-50%);
    text-align: center;
    font-weight: 700;
    font-size: 50px;
    line-height: 1.1;
    letter-spacing: 2px;
  }
  .front-dark .front-name { color: var(--silver); }
  .front-light .front-name { color: var(--silver-dark); }

  /* Back faces */
  .back-dark {
    left: 21px; top: 398px; width: 567px; height: 316px;
    background: var(--ink-dark); color: var(--text-on-dark);
  }
  .back-light {
    left: 613px; top: 398px; width: 557px; height: 316px;
    background: var(--ink-light); color: var(--text-on-light);
  }
  .person-name {
    position: absolute; left: 34px; top: 44px;
    font-size: 24px; font-weight: 700; letter-spacing: 0.5px;
  }
  .contact-list {
    position: absolute; left: 34px; top: 122px;
    list-style: none; font-size: 14px; line-height: 19px;
  }
  .contact-list li { display: flex; align-items: center; gap: 8px; }
  .contact-list svg { width: 16px; height: 14px; flex: none; }
  .contact-list .small { font-size: 10px; line-height: 15px; }
  .back-name {
    position: absolute; right: 30px; top: 180px;
    width: 200px; text-align: center;
    font-size: 24px; font-weight: 700; line-height: 1.1;
  }
  .back-dark .back-name { color: var(--silver); }
  .back-light .back-name { color: var(--silver-dark); }
  .services {
    position: absolute; left: 32px; right: 28px; bottom: 16px;
    display: flex; justify-content: space-between; align-items: baseline;
    font-size: 13px;
  }
  .services .lead { margin-right: 30px; }
  .back-dark .services .lead { color: var(--muted-on-dark); }
  .back-light .services .lead { color: var(--muted-on-light); }
  .services ul { display: flex; gap: 26px; list-style: none; }
</style>
</head>
<body>

<section class="card front-dark" aria-label="Front, dark version">
  <p class="front-name">Torvane<br>Construction</p>
</section>

<section class="card front-light" aria-label="Front, light version">
  <p class="front-name">Torvane<br>Construction</p>
</section>

<section class="card back-dark" aria-label="Back, dark version">
  <h1 class="person-name">Your Name Here</h1>
  <ul class="contact-list">
    <li><svg viewBox="0 0 16 14"><path d="M2 7 8 2l6 5M4 6v7h8V6" fill="none" stroke="currentColor" stroke-width="1.5"/></svg><span>PO Box 8640 Dunmore QLD 4170</span></li>
    <li><svg viewBox="0 0 16 14"><rect x="1" y="2" width="14" height="10" fill="currentColor"/></svg><span>person@torvaneconstruction.example.au</span></li>
    <li><svg viewBox="0 0 16 14"><circle cx="8" cy="7" r="6" fill="none" stroke="currentColor" stroke-width="1.5"/><path d="M2 7h12M8 1v12" stroke="currentColor"/></svg><span>www.torvaneconstruction.example.au</span></li>
    <li><svg viewBox="0 0 16 14"><path d="M1 5q7-5 14 0v2h-3V5H4v2H1zM3 8h10v5H3z" fill="currentColor"/></svg><span>333 507 214</span></li>
    <li><svg viewBox="0 0 16 14"><rect x="2" y="5" width="12" height="8" fill="currentColor"/><rect x="4" y="1" width="8" height="4" fill="none" stroke="currentColor"/></svg><span>333 507 869</span></li>
    <li class="small"><span>BSA license: xxx-xxxx</span></li>
    <li class="small"><span>ABN: 47209836512</span></li>
  </ul>
  <p class="back-name">Torvane<br>Construction</p>
  <div class="services">
    <span class="lead">Licensed buiders specialising in</span>
    <ul><li>Bathrooms</li><li>Kitchens</li><li>Comercial Interiors</li></ul>
  </div>
</section>

<section class="card back-light" aria-label="Back, light version">
  <h1 class="person-name">Your Name Here</h1>
  <ul class="contact-list">
    <li><svg viewBox="0 0 16 14"><path d="M2 7 8 2l6 5M4 6v7h8V6" fill="none" stroke="currentColor" stroke-width="1.5"/></svg><span>PO Box 8640 Dunmore QLD 4170</span></li>
    <li><svg viewBox="0 0 16 14"><rect x="1" y="2" width="14" height="10" fill="currentColor"/></svg><span>person@torvaneconstruction.example.au</span></li>
    <li><svg viewBox="0 0 16 14"><circle cx="8" cy="7" r="6" fill="none" stroke="currentColor" stroke-width="1.5"/><path d="M2 7h12M8 1v12" stroke="currentColor"/></svg><span>www.torvaneconstruction.example.au</span></li>
    <li><svg viewBox="0 0 16 14"><path d="M1 5q7-5 14 0v2h-3V5H4v2H1zM3 8h10v5H3z" fill="currentColor"/></svg><span>333 507 214</span></li>
    <li><svg viewBox="0 0 16 14"><rect x="2" y="5" width="12" height="8" fill="currentColor"/><rect x="4" y="1" width="8" height="4" fill="none" stroke="currentColor"/></svg><span>333 507 869</span></li>
    <li class="small"><span>BSA license: xxx-xxxx</span></li>
    <li class="small"><span>ABN: 47209836512</span></li>
  </ul>
  <p class="back-name">Torvane<br>Construction</p>
  <div class="services">
    <span class="lead">Licensed buiders specialising in</span>
    <ul><li>Bathrooms</li><li>Kitchens</li><li>Comercial Interiors</li></ul>
  </div>
</section>

</body>
</html>
```